Marisol Dune - Australia's Sexiest Lingerie

Dear designer!
Myself and my business partner Mari Holloway (google her or checkout her insta account @mariholloway) are launching a new lingerie company called Marisol Dune in 4 months and are in dire need of quality graphic design. If we like your designs we'd love to grow our brand with you and hopefully you'd be proud to have us in your portfolio. We're expecting big things very soon!
We like the idea of cursive writing (script fonts). Something very elegant to match an elegant name - Marisol Dune.
https://larkspurintimates.example and http://hollowtideunderwear.example are two designs that appeal to us.
Our slogan is "Australia's Sexiest Lingerie" and our 2 logo's are the initials "MD" and what they stand for "Marisol Dune". The "MD" will eventually be used on all the products as a jewellery charm. Please incorporate these into the web design somehow.
The final design should be simple and beautiful.
Thanks very much designer, we look forward to seeing your work!
Updates
We have some fantastic results so far, thank you for the submissions. For those yet to submit, please know that the best design will receive our ongoing business directly. Still 2 weeks to pick the best. We look forward to seeing your piece of art. Added Sunday, June 7, 2015
Target Market(s)
Women 18 - 35
Industry/Entity Type
Retail
Contact Information for Business Card
CARD 1:
Marisol Dune Pty Ltd
(Logo)
Colin Brevik
Co-founder and Director
0431 857 204
colin@marisol-dune.example
CARD 2:
Marisol Dune Pty Ltd
(Logo)
Marisol Dune Holloway
Co-founder and Director
0417 263 590
mari@marisol-dune.example
Logo Text
Australia's Sexiest Lingerie
Coding
Coded - Design and coding required
Number of Pages Required
1 page
Requirements
Must have
- 1 x 'MD" Logo
- 1 x 'Marisol Dune' Logo
- 1 x 'Australia's Sexiest Lingerie' Slogan

```html
<!DOCTYPE html>
<html lang="en">
<head>
<meta charset="utf-8">
<title>Marisol Dune – Australia's Sexiest Lingerie</title>
<link rel="stylesheet" href="https://fonts.googleapis.com/css2?family=Great+Vibes&family=Montserrat:wght@400;600;700;800&family=Open+Sans:wght@400;600;700&display=swap">
<style>
:root{
  --ink:#111111;
  --white:#ffffff;
  --hero-dark:#262626;
  --hero-mid:#3d3d3d;
  --body-text:#555555;
  --accent-pink:#b6479b;
  --accent-green:#3fae6f;
  --summer-navy:#1d3a55;
  --autumn-green:#5bc08a;
  --card-grey:#eeeeee;
  --wave-grey:#f4f4f4;
  --footer-pink:#e6ccd3;
}
*{margin:0;padding:0;box-sizing:border-box}
html,body{width:1200px;height:3084px;overflow:hidden;background:var(--white)}
body{position:relative;font-family:'Open Sans',Arial,sans-serif;color:var(--ink)}
.abs{position:absolute}

/* Hero */
.hero{left:0;top:0;width:1200px;height:591px;
  background:
    radial-gradient(ellipse 200px 300px at 560px 330px,rgba(235,235,235,.55) 0%,rgba(200,200,200,.25) 45%,rgba(0,0,0,0) 100%),
    radial-gradient(ellipse 120px 160px at 600px 110px,rgba(160,160,160,.45) 0%,rgba(0,0,0,0) 100%),
    linear-gradient(90deg,rgba(0,0,0,.35) 0%,rgba(0,0,0,0) 30%,rgba(0,0,0,0) 70%,rgba(0,0,0,.35) 100%),
    linear-gradient(180deg,#3a3a3a 0%,var(--hero-mid) 50%,var(--hero-dark) 100%)}
.nav{left:44px;top:34px;display:flex;gap:30px;font-family:'Montserrat',Arial,sans-serif;font-weight:700;font-size:12px;color:var(--white);letter-spacing:.5px}
.nav .active{border-bottom:2px solid var(--white);padding-bottom:10px}
.brand{left:450px;top:20px;width:300px;text-align:center;color:var(--white)}
.brand-name{font-family:'Great Vibes',cursive;font-size:46px;line-height:1}
.brand-tag{font-size:10px;letter-spacing:1px;margin-top:0}
.tools{left:1052px;top:28px;display:flex;gap:18px;align-items:center}

/* Intro */
.monogram{left:500px;top:630px;width:200px;text-align:center;font-family:'Great Vibes',cursive;font-size:96px;line-height:1.1}
.one-liner{left:400px;top:754px;width:400px;text-align:center;font-size:11px;letter-spacing:.5px;color:#333}
.intro-copy{left:345px;top:790px;width:510px;text-align:center;font-size:11.5px;line-height:1.6;color:var(--body-text)}
.intro-copy p{margin-bottom:14px}
.catchy{left:400px;top:1020px;width:400px;text-align:center;font-family:'Montserrat',Arial,sans-serif;font-weight:800;font-size:33px;line-height:36px;letter-spacing:.5px}

/* Band */
.band{left:0;top:1230px;width:1200px;height:356px;
  background:
    radial-gradient(ellipse 220px 110px at 390px 210px,rgba(250,246,242,.95) 0%,rgba(240,230,222,.6) 50%,rgba(0,0,0,0) 100%),
    radial-gradient(ellipse 260px 90px at 700px 190px,rgba(248,242,238,.9) 0%,rgba(235,225,218,.5) 55%,rgba(0,0,0,0) 100%),
    radial-gradient(ellipse 90px 60px at 300px 150px,rgba(232,196,150,.9) 0%,rgba(0,0,0,0) 100%),
    linear-gradient(180deg,rgba(0,0,0,0) 55%,rgba(210,200,195,.55) 80%,rgba(150,140,135,.5) 100%),
    linear-gradient(90deg,#6e3a12 0%,#b0772e 10%,#7a3d1c 20%,#5a2a18 35%,#6a2e22 60%,#7c2e26 80%,#5a2016 100%)}

/* Collections */
.collections-title{left:0;top:1626px;width:1200px;text-align:center;font-family:'Montserrat',Arial,sans-serif;font-weight:700;font-size:21px;letter-spacing:.5px;color:var(--accent-pink)}
.collection{top:1696px;width:418px;height:445px;background:var(--card-grey);overflow:hidden}
.collection .art{position:absolute;left:70px;top:22px;width:280px;height:423px;border-radius:140px 140px 0 0}
.collection .label{position:absolute;left:0;bottom:10px;width:100%;text-align:center;font-family:'Montserrat',Arial,sans-serif;font-weight:800;font-size:52px;letter-spacing:1px}
.summer .art{background:linear-gradient(180deg,#a4b4c0 0%,#6d8ea0 30%,#3e7e8e 50%,#c79b5a 72%,#d9b272 100%)}
.summer .label{color:var(--summer-navy)}
.autumn .art{background:linear-gradient(180deg,#b5b9ae 0%,#7c8c74 35%,#4b5e46 60%,#3a4434 100%)}
.autumn .label{color:var(--autumn-green)}

/* Shipping */
.waves{left:0;top:2210px;width:1200px;height:260px;background:linear-gradient(180deg,var(--white) 0%,var(--wave-grey) 35%,var(--wave-grey) 70%,var(--white) 100%)}
.ship-small{left:0;top:2264px;width:1200px;text-align:center;font-family:'Montserrat',Arial,sans-serif;font-weight:700;font-size:16px;letter-spacing:6px}
.ship-big{left:0;top:2286px;width:1200px;text-align:center;font-family:'Montserrat',Arial,sans-serif;font-weight:800;font-size:64px;letter-spacing:14px}
.badge{left:564px;top:2376px;width:72px;height:72px;border-radius:50%;background:var(--accent-green);color:var(--white);text-align:center;font-family:'Montserrat',Arial,sans-serif}
.badge small{display:block;font-size:7px;font-weight:600;margin-top:15px;line-height:1.2}
.badge b{display:block;font-size:17px;font-weight:800;line-height:1.1}

/* Products */
.product{top:2506px;width:238px;height:360px}
.product-card{border:5px solid var(--ink);background:
  radial-gradient(ellipse 70px 110px at 50% 30%,rgba(230,220,205,.7) 0%,rgba(0,0,0,0) 100%),
  linear-gradient(180deg,#e9f1ec 0%,#f6f8f6 55%,#ffffff 100%)}
.product-card .heart{position:absolute;left:104px;top:100px}
.product-name{position:absolute;left:0;top:150px;width:100%;text-align:center;font-family:'Montserrat',Arial,sans-serif;font-weight:700;font-size:11px;color:var(--accent-green)}
.price{position:absolute;left:0;top:174px;width:100%;text-align:center;font-size:11px}
.price s{color:#888;margin-right:8px}
.price span{color:var(--accent-green)}
.add-btn{position:absolute;left:58px;top:205px;width:112px;height:38px;border:4px solid #8a8a8a;font-family:'Montserrat',Arial,sans-serif;font-weight:700;font-size:8.5px;display:flex;align-items:center;justify-content:center;background:var(--white)}
.product-photo{border:1px solid #cccccc}
.photo-a{background:
  radial-gradient(ellipse 60px 150px at 50% 62%,rgba(200,70,60,.85) 0%,rgba(0,0,0,0) 100%),
  linear-gradient(180deg,#4f7a3e 0%,#8aa86a 30%,#b98a6a 45%,#8e9e5a 100%)}
.photo-b{background:
  radial-gradient(ellipse 50px 150px at 50% 55%,rgba(214,176,140,.9) 0%,rgba(0,0,0,0) 100%),
  linear-gradient(180deg,#6fb0dc 0%,#a9d3ec 35%,#3d7fa6 55%,#7ba6b5 65%,#e4d6bc 80%,#efe5d2 100%)}
.view-all{left:522px;top:2920px;width:160px;height:52px;border:4px solid #8a8a8a;display:flex;align-items:center;justify-content:center;font-family:'Montserrat',Arial,sans-serif;font-weight:700;font-size:10px}

/* Footer */
.footer{left:0;top:3012px;width:1200px;height:72px;background:var(--footer-pink);font-size:9px;color:#6a5a5e}
.copyright{left:80px;top:32px}
.quick-shop{left:550px;top:18px;width:100px;text-align:center;font-size:8px;letter-spacing:.5px}
.dots{display:flex;justify-content:center;gap:4px;margin-bottom:6px}
.dots i{width:6px;height:6px;border:1px solid #6a5a5e;border-radius:50%}
.payments{left:790px;top:29px;display:flex;gap:22px;font-weight:700;font-size:11px;color:#6a5a5e}
</style>
</head>
<body>

<section class="abs hero" role="img" aria-label="Black and white photograph of a model seen from behind in lingerie"></section>
<nav class="abs nav"><span class="active">INFO</span><span>COLLECTION</span><span>SHOP</span><span>STOCKISTS</span></nav>
<div class="abs brand"><div class="brand-name">Marisol Dune</div><div class="brand-tag">Australia's Sexiest Lingerie</div></div>
<div class="abs tools">
  <svg width="20" height="18" viewBox="0 0 20 18" aria-label="Wishlist"><path d="M10 16 L2.5 8.5 A4.5 4.5 0 0 1 10 3 A4.5 4.5 0 0 1 17.5 8.5 Z" fill="none" stroke="#fff" stroke-width="2"/></svg>
  <svg width="18" height="18" viewBox="0 0 18 18" aria-label="Search"><circle cx="7.5" cy="7.5" r="5.5" fill="none" stroke="#fff" stroke-width="2.2"/><line x1="11.5" y1="11.5" x2="16.5" y2="16.5" stroke="#fff" stroke-width="2.6"/></svg>
  <svg width="22" height="24" viewBox="0 0 22 24" aria-label="Cart"><path d="M7 7 V5 A4 4 0 0 1 15 5 V7" fill="none" stroke="#fff" stroke-width="2"/><rect x="2" y="7" width="18" height="16" fill="#fff"/><text x="11" y="19" font-family="Montserrat,Arial,sans-serif" font-size="10" font-weight="700" text-anchor="middle" fill="#2a2a2a">0</text></svg>
</div>

<div class="abs monogram">MD</div>
<div class="abs one-liner">SOME ONE LINER HERE</div>
<div class="abs intro-copy">
  <p>[Example text] sit amet, consectetur adipiscing elit. Nunc viverra pretium libero, eu sagittis tellus imperdiet efficitur. Nulla ultrices ipsum sed ligula sagittis, eu posuere risus mattis. Vestibulum purus ligula, feugiat. Nunc viverra pretium libero.</p>
  <p>Aliquam ultrices venenatis nisi. Vivamus auctor nulla at gravida vehicula. Etiam et tortor ut ipsum mattis scelerisque. Quisque consectetur odio metus, at eleifend leo scelerisque et proin sagittis.</p>
  <p>Morbi mauris sem, maximus eget ligula eu, sodales molestie elit. Aliquam euismod efficitur tortor, ullamcorper tempor felis elementum nec. Suspendisse id libero eros. Vestibulum est justo, fringilla nec purus.</p>
</div>
<h2 class="abs catchy">WRITE SOME<br>CATCHY TEXT HERE,<br>MAKE IT VERY<br>INSPIRING ;)</h2>

<section class="abs band" role="img" aria-label="Photograph of a model in white lingerie reclining on a bed in a warm wood-panelled room"></section>

<h3 class="abs collections-title">COLLECTIONS - SUMMER/AUTUMN 2015</h3>
<div class="abs collection summer" style="left:162px"><div class="art" role="img" aria-label="Double exposure of a silhouette with a mountain lake landscape"></div><div class="label">SUMMER</div></div>
<div class="abs collection autumn" style="left:604px"><div class="art" role="img" aria-label="Double exposure of a silhouette with a forest landscape"></div><div class="label">AUTUMN</div></div>

<div class="abs waves" role="img" aria-label="Soft wavy line background pattern"></div>
<div class="abs ship-small">FREE SHIPPING</div>
<div class="abs ship-big">WORLDWIDE</div>
<div class="abs badge"><small>ORDERS<br>OVER</small><b>$100</b></div>

<article class="abs product product-card" style="left:85px" aria-label="Product card with faded model photograph">
  <svg class="heart" width="20" height="18" viewBox="0 0 20 18"><path d="M10 16 L2.5 8.5 A4.5 4.5 0 0 1 10 3 A4.5 4.5 0 0 1 17.5 8.5 Z" fill="none" stroke="#111" stroke-width="2"/></svg>
  <div class="product-name">ENTER PRODUCT NAME HERE</div>
  <div class="price"><s>£55.00</s><span>£35.00</span></div>
  <div class="add-btn">ADD TO CART</div>
</article>
<div class="abs product product-photo photo-a" style="left:350px" role="img" aria-label="Photograph of a model in a printed playsuit among palm leaves"></div>
<article class="abs product product-card" style="left:617px" aria-label="Product card with faded model photograph">
  <svg class="heart" width="20" height="18" viewBox="0 0 20 18"><path d="M10 16 L2.5 8.5 A4.5 4.5 0 0 1 10 3 A4.5 4.5 0 0 1 17.5 8.5 Z" fill="none" stroke="#111" stroke-width="2"/></svg>
  <div class="product-name">ENTER PRODUCT NAME HERE</div>
  <div class="price"><s>£55.00</s><span>£35.00</span></div>
  <div class="add-btn">ADD TO CART</div>
</article>
<div class="abs product product-photo photo-b" style="left:882px" role="img" aria-label="Photograph of a model in a bikini on a beach"></div>

<div class="abs view-all">VIEW ALL PRODUCTS</div>

<footer class="abs footer">
  <div class="abs copyright">COPYRIGHT 2015 MARISOL DUNE. ALL RIGHTS RESERVED</div>
  <div class="abs quick-shop"><div class="dots"><i></i><i></i><i></i></div>QUICK SHOP</div>
  <div class="abs payments"><span>Varda</span><span>Meridian</span><span>Paywell</span><span>Dovecote</span><span>Amberly</span><span>Strata</span></div>
</footer>

</body>
</html>
```